Website for a new investor-focused estate agency portal

Require a website for a new investor-focused estate agency portal, this will interface with our exisitng API for data posting and retrieval. We have a logo for the business, but will happily change the colour palette to suit the design.
Requirements:
1) Landing page to describe the business
- Feature line showing the latest properties in our listings
- Announcement section (e.g. mobile app coming soon)
- Text area - what we do for Investors
- Text area - what we do for Agents and sourcers
- Text area - what we do for Home buyers
- Small Q&A
- Subscription pricing description and sign up
2) Content page (product updates page)
A timeline to list list releases, new features and other improvements to the service, website and app, shown in most recent date order.
3) A property search/result page including search form
4) A single property detail page, including
- carousel for images and video
- map
- text content
5) A data entry page to enter property data into the system. This page will contain a sidebar menu, property name, address, description, and about 10 other fields (detail to be provided). The attached screen dump files are snapshot of the wireframe form used by the development team for the property entry page.
Target Market(s)
Property investors / Real estate buyer's including personal home buyers.
Number of Pages Required
5+ page
Colors
Designer to choose colors to be used in the design.
Requirements
Must have
- Clean, crisp design and presentaion.
Nice to have
- The Search/result page (3) and the detail page (4) may have 2-3 elements for paid advertising but should also look good without those elements.
Should not have
- Must not be too busy with distracting elements

```html
<!DOCTYPE html>
<html lang="en">
<head>
<meta charset="utf-8">
<title>Ridgeline Homes – Find the perfect home</title>
<link href="https://fonts.googleapis.com/css2?family=Fira+Sans:wght@400;500;600&display=swap" rel="stylesheet">
<style>
  :root {
    --nav-bg: #3a7291;
    --nav-bg-end: #4a7d99;
    --text-light: #ffffff;
    --panel-bg: rgba(28, 58, 84, 0.62);
    --tab-line: rgba(255, 255, 255, 0.45);
    --tab-active: #8ec3ea;
    --field-blue: #5b9fd4;
    --field-divider: rgba(255, 255, 255, 0.35);
    --search-btn: #111418;
    --placeholder: #9aa3ab;
    --page-bg: #eceff1;
  }
  * { box-sizing: border-box; margin: 0; padding: 0; }
  html, body { width: 1200px; height: 703px; overflow: hidden; background: var(--page-bg); }
  body { font-family: "Fira Sans", sans-serif; color: var(--text-light); position: relative; }

  .site-header {
    position: absolute; left: 0; top: 0; width: 1200px; height: 118px;
    background: linear-gradient(90deg, var(--nav-bg), var(--nav-bg-end));
  }
  .nav-link {
    position: absolute; top: 52px; font-size: 13px; font-weight: 600;
    transform: translateX(-50%); white-space: nowrap; color: var(--text-light); text-decoration: none;
  }
  .brand {
    position: absolute; left: 603px; top: 35px; transform: translateX(-50%);
    width: 96px; display: flex; align-items: center; gap: 6px;
  }
  .brand-square { flex: none; width: 10px; height: 10px; background: var(--text-light); }
  .brand-name {
    font-size: 17px; font-weight: 600; line-height: 22px; white-space: nowrap;
  }

  .hero {
    position: absolute; left: 0; top: 118px; width: 1200px; height: 585px;
    background:
      linear-gradient(180deg, rgba(20,32,45,0.55) 0%, rgba(20,32,45,0.25) 40%, rgba(15,35,60,0.35) 100%),
      linear-gradient(180deg, #3f4a52 0%, #7d7a6c 30%, #a4815a 48%, #5f6d78 62%, #2f6e9c 78%, #1f4f7c 100%);
  }
  .hero-title {
    position: absolute; left: 0; width: 1200px; top: 170px; text-align: center;
    font-size: 27px; font-weight: 600; letter-spacing: 0.2px;
    text-shadow: 0 1px 3px rgba(0,0,0,0.35);
  }

  .search-panel {
    position: absolute; left: 245px; top: 234px; width: 717px; height: 178px;
    background: var(--panel-bg);
  }
  .search-tabs { display: flex; height: 45px; border-bottom: 2px solid var(--tab-line); }
  .search-tab {
    flex: 1; text-align: center; line-height: 43px; font-size: 14px; font-weight: 400;
  }
  .search-tab.is-active { border-bottom: 3px solid var(--tab-active); margin-bottom: -2px; }
  .search-row { position: absolute; left: 12px; top: 60px; width: 691px; height: 31px; display: flex; }
  .search-input {
    flex: 1; background: #fff; color: var(--placeholder); font-size: 12px;
    line-height: 31px; padding-left: 8px;
  }
  .search-button {
    width: 111px; background: var(--search-btn); font-size: 12px;
    display: flex; align-items: center; justify-content: center; gap: 5px;
  }
  .filter-row { position: absolute; left: 12px; top: 105px; width: 691px; height: 65px; display: flex; background: var(--field-blue); }
  .filter {
    flex: 1; position: relative; padding: 12px 0 0 12px;
    border-right: 1px solid var(--field-divider);
  }
  .filter:last-child { border-right: none; }
  .filter-label { font-size: 11px; opacity: 0.9; }
  .filter-value { font-size: 13px; font-weight: 500; margin-top: 6px; }
  .filter-chevron { position: absolute; right: 12px; top: 30px; }

  .slider-arrow { position: absolute; top: 288px; }
  .slider-arrow.prev { left: 82px; }
  .slider-arrow.next { left: 1105px; }

  .slider-dots { position: absolute; top: 490px; left: 603px; transform: translateX(-50%); display: flex; gap: 6px; }
  .dot { width: 8px; height: 8px; background: #fff; transform: rotate(45deg); }
  .dot.is-current { background: var(--tab-active); }
</style>
</head>
<body>
  <header class="site-header">
    <a class="nav-link" style="left:210px">For sale</a>
    <a class="nav-link" style="left:298px">To rent</a>
    <a class="nav-link" style="left:402px">House prices</a>
    <a class="nav-link" style="left:500px">Invest</a>
    <div class="brand"><span class="brand-square"></span><span class="brand-name">Ridgeline<br>Homes</span></div>
    <a class="nav-link" style="left:708px">New homes</a>
    <a class="nav-link" style="left:807px">Commercial</a>
    <a class="nav-link" style="left:897px">Overseas</a>
    <a class="nav-link" style="left:987px">Find agents</a>
  </header>

  <section class="hero" role="img" aria-label="Modern white villa with glass walls and an illuminated swimming pool at dusk">
    <h1 class="hero-title">Find the perfect home to buy or rent in the UK</h1>

    <svg class="slider-arrow prev" width="20" height="40" viewBox="0 0 20 40" aria-hidden="true">
      <polyline points="17,2 3,20 17,38" fill="none" stroke="#fff" stroke-width="2"/>
    </svg>
    <svg class="slider-arrow next" width="20" height="40" viewBox="0 0 20 40" aria-hidden="true">
      <polyline points="3,2 17,20 3,38" fill="none" stroke="#fff" stroke-width="2"/>
    </svg>

    <form class="search-panel">
      <div class="search-tabs">
        <div class="search-tab is-active">For sale</div>
        <div class="search-tab">To rent</div>
        <div class="search-tab">Find agents</div>
        <div class="search-tab">Sold prices</div>
      </div>
      <div class="search-row">
        <div class="search-input">e.g. Bristol, SW6, G61 2DW, Victoria Station</div>
        <div class="search-button">
          <svg width="11" height="11" viewBox="0 0 12 12" aria-hidden="true">
            <circle cx="5" cy="5" r="3.8" fill="none" stroke="#fff" stroke-width="1.3"/>
            <line x1="7.8" y1="7.8" x2="11" y2="11" stroke="#fff" stroke-width="1.3"/>
          </svg>Search
        </div>
      </div>
      <div class="filter-row">
        <div class="filter"><div class="filter-label">Min price ($)</div><div class="filter-value">Any</div>
          <svg class="filter-chevron" width="14" height="9" viewBox="0 0 14 9" aria-hidden="true"><polyline points="1,1 7,7 13,1" fill="none" stroke="#fff" stroke-width="2"/></svg></div>
        <div class="filter"><div class="filter-label">Max price ($)</div><div class="filter-value">Any</div>
          <svg class="filter-chevron" width="14" height="9" viewBox="0 0 14 9" aria-hidden="true"><polyline points="1,1 7,7 13,1" fill="none" stroke="#fff" stroke-width="2"/></svg></div>
        <div class="filter"><div class="filter-label">Property type</div><div class="filter-value">Any</div>
          <svg class="filter-chevron" width="14" height="9" viewBox="0 0 14 9" aria-hidden="true"><polyline points="1,1 7,7 13,1" fill="none" stroke="#fff" stroke-width="2"/></svg></div>
        <div class="filter"><div class="filter-label">Bed rooms</div><div class="filter-value">Any</div>
          <svg class="filter-chevron" width="14" height="9" viewBox="0 0 14 9" aria-hidden="true"><polyline points="1,1 7,7 13,1" fill="none" stroke="#fff" stroke-width="2"/></svg></div>
      </div>
    </form>

    <div class="slider-dots">
      <span class="dot"></span><span class="dot is-current"></span><span class="dot"></span>
    </div>
  </section>
</body>
</html>
```